Parkinson's Disease Progression

Visually describe the rate of Parkinson progression in the first 15 years following diagnosis. Title: "Patient-Perceived Progression of Parkinsonism"

The attached figure names "meanqol" is the curve that should serve as the basis of this graphic. Everything else-- color, labels, font, etc. describe this curve.
Thank you!

Target Market(s)

People with Parkisnon's Disease, neurologists, family members.

Font styles to use
Sans Serif

Requirements
Must have
• Must have the lines going through these exact numbers
Excellent -- 502
Very good- 661
Good- 895
Fair- 1268
Poor- 1655

LABELS:
Title: "Patient-Perceived Progression of Parkinsonism"
"SWI-TC (Self-Logged Wellbeing Index for Tremor Conditions)" should be the label on the left.
"Quality of Life" should be the label on the right
"Years Since Diagnosis" should be the label on the bottom
Nice to have
• A color scheme that goes from GOOD (low numbers) to BAD (high numbers).

Easy to read (elderly)

```html
<!DOCTYPE html>
<html lang="en">
<head>
<meta charset="utf-8">
<title>Patient-Perceived Progression of Parkinsonism</title>
<link rel="stylesheet" href="https://fonts.googleapis.com/css2?family=Barlow+Semi+Condensed:wght@400;600;700&display=swap">
<style>
  :root {
    --paper: #ffffff;
    --ink: #111111;
    --band-poor: #f7a68d;
    --band-fair: #fbc590;
    --band-good: #fdf39d;
    --band-very-good: #d6e5b6;
    --band-excellent: #b6d8f0;
    --divider: #ffffff;
  }
  html, body {
    margin: 0;
    padding: 0;
    width: 1200px;
    height: 848px;
    overflow: hidden;
    background: var(--paper);
  }
  .chart {
    display: block;
    width: 1200px;
    height: 848px;
    font-family: "Barlow Semi Condensed", "Arial Narrow", sans-serif;
  }
  .chart-title {
    font-weight: 700;
    font-size: 23px;
    fill: var(--ink);
  }
  .axis-title {
    font-weight: 400;
    font-size: 19px;
    letter-spacing: 0.5px;
    fill: var(--ink);
  }
  .tick-label {
    font-weight: 600;
    font-size: 13px;
    fill: var(--ink);
  }
  .band-tag-box { fill: var(--paper); }
  .band-tag {
    font-weight: 700;
    font-size: 12.5px;
    fill: var(--ink);
  }
  .band-poor { fill: var(--band-poor); }
  .band-fair { fill: var(--band-fair); }
  .band-good { fill: var(--band-good); }
  .band-very-good { fill: var(--band-very-good); }
  .band-excellent { fill: var(--band-excellent); }
  .band-divider {
    stroke: var(--divider);
    stroke-width: 1.2;
    stroke-dasharray: 1.5 2;
  }
  .axis-line { stroke: var(--ink); stroke-width: 5; }
  .axis-tick { stroke: var(--ink); stroke-width: 1.5; }
  .mean-curve { fill: none; stroke: var(--ink); stroke-width: 3; stroke-linecap: round; }
  .confidence-edge { fill: none; stroke: var(--ink); stroke-width: 1; stroke-dasharray: 3 2.5; }
</style>
</head>
<body>
<svg class="chart" viewBox="0 0 850 600" preserveAspectRatio="none" role="img" aria-label="Line chart of patient-perceived progression of parkinsonism over 15 years since diagnosis">
  <defs>
    <linearGradient id="tail-fade" x1="0" y1="0" x2="1" y2="0">
      <stop offset="0" stop-color="#ffffff" stop-opacity="0"/>
      <stop offset="0.5" stop-color="#ffffff" stop-opacity="0.5"/>
      <stop offset="1" stop-color="#ffffff" stop-opacity="0.85"/>
    </linearGradient>
  </defs>

  <text class="chart-title" x="415" y="69" text-anchor="middle" textLength="624" lengthAdjust="spacingAndGlyphs">PATIENT-PERCEIVED PROGRESSION OF PARKINSONISM</text>

  <!-- quality bands -->
  <rect class="band-poor" x="190" y="108" width="495" height="94"/>
  <rect class="band-fair" x="190" y="202" width="495" height="86"/>
  <rect class="band-good" x="190" y="288" width="495" height="54"/>
  <rect class="band-very-good" x="190" y="342" width="495" height="37"/>
  <rect class="band-excellent" x="190" y="379" width="495" height="111"/>
  <line class="band-divider" x1="190" y1="202" x2="685" y2="202"/>
  <line class="band-divider" x1="190" y1="288" x2="685" y2="288"/>
  <line class="band-divider" x1="190" y1="342" x2="685" y2="342"/>
  <line class="band-divider" x1="190" y1="379" x2="685" y2="379"/>

  <!-- confidence region -->
  <path d="M205,368 C250,350 295,322 347,318 C380,315 405,318 435,306 C480,288 510,268 550,252 C585,237 610,226 628,211 L685,203 L685,287 L628,273 C610,268 590,263 560,266 C520,272 500,286 470,300 C440,313 410,330 347,333 C300,336 250,360 205,415 Z" fill="#ffffff" fill-opacity="0.35"/>
  <rect x="600" y="203" width="85" height="84" fill="url(#tail-fade)"/>
  <path class="confidence-edge" d="M205,368 C250,350 295,322 347,318 C380,315 405,318 435,306 C480,288 510,268 550,252 C585,237 610,226 628,211"/>
  <path class="confidence-edge" d="M205,415 C240,370 290,338 347,333 C400,329 420,326 450,310 C490,289 515,274 555,266 C590,259 612,262 628,273"/>
  <path class="mean-curve" d="M205,393 C245,370 295,332 347,326 C380,322 400,330 430,316 C470,300 500,283 540,262 C575,250 605,247 628,243"/>

  <!-- band tags -->
  <rect class="band-tag-box" x="633" y="179" width="52" height="18"/>
  <text class="band-tag" x="659" y="193" text-anchor="middle">POOR</text>
  <text class="band-tag" x="659" y="279" text-anchor="middle">FAIR</text>
  <rect class="band-tag-box" x="606" y="321" width="79" height="18"/>
  <text class="band-tag" x="659" y="335" text-anchor="middle">GOOD</text>
  <rect class="band-tag-box" x="601" y="357" width="84" height="18"/>
  <text class="band-tag" x="643" y="371" text-anchor="middle">VERY GOOD</text>
  <rect class="band-tag-box" x="601" y="461" width="84" height="18"/>
  <text class="band-tag" x="643" y="475" text-anchor="middle">EXCELLENT</text>

  <!-- axes -->
  <line class="axis-line" x1="190" y1="108" x2="190" y2="492"/>
  <line class="axis-line" x1="188" y1="490" x2="685" y2="490"/>
  <line class="axis-tick" x1="347" y1="490" x2="347" y2="498"/>
  <line class="axis-tick" x1="488" y1="490" x2="488" y2="498"/>
  <line class="axis-tick" x1="628" y1="490" x2="628" y2="498"/>

  <g class="tick-label" text-anchor="end">
    <text x="172" y="130">1600</text>
    <text x="172" y="176">1400</text>
    <text x="172" y="222">1200</text>
    <text x="172" y="269">1000</text>
    <text x="172" y="315">800</text>
    <text x="172" y="361">600</text>
    <text x="172" y="407">400</text>
    <text x="172" y="454">200</text>
  </g>
  <g class="tick-label" text-anchor="middle">
    <text x="205" y="523">0</text>
    <text x="347" y="523">5</text>
    <text x="488" y="523">10</text>
    <text x="628" y="523">15</text>
  </g>

  <text class="axis-title" x="430" y="554" text-anchor="middle" textLength="238" lengthAdjust="spacingAndGlyphs">YEARS SINCE DIAGNOSIS</text>
  <text class="axis-title" transform="translate(121 302) rotate(-90)" text-anchor="middle">SELF-LOGGED WELLBEING</text>
  <text class="axis-title" transform="translate(727 299) rotate(-90)" text-anchor="middle" textLength="158" lengthAdjust="spacingAndGlyphs">QUALITY OF LIFE</text>
</svg>
</body>
</html>
```